Book cover required for new book business book (Otter Ambush SEO for Managed Service Providers)

We are finalizing publishing dates for our latest business book. The audience this book is targetting is IT business owners. Demographic age 30-50 years of age, male, middle class. The title of the book is Otter Ambush SEO for managed service providers. The author name is Dean Harrow. The book goes into details about how to improve SEO for IT businesses. The premise of the book is if a bear attacked a crowd of people, and you were in that crowd, you'd only have to be 1% faster to outrun the bear. The same is true for your IT Businesses website. You only have to put in 1% more effort into your SEO to be on page one of Zarvio.
We have been using a working draft image whilst the book has been in preproduction. I am unsure if this working image is licensed. Please find attached.

```html
<!DOCTYPE html>
<html lang="en">
<head>
<meta charset="utf-8">
<title>Otter Ambush SEO for Managed Service Providers — Dean Harrow</title>
<link rel="stylesheet" href="https://fonts.googleapis.com/css2?family=Montserrat:ital,wght@0,300;0,400;0,500;0,800;1,500&display=swap">
<style>
  :root {
    --page-bg: #e9eaec;
    --cover-bg: #f3f3f3;
    --ink-grey: #4b4b4d;
    --brand-blue: #1e5ea8;
    --brand-blue-deep: #16468a;
    --photo-light: #c9c4c4;
    --photo-mid: #a48c8a;
    --photo-dark: #3f3a3c;
    --white: #ffffff;
  }
  * { box-sizing: border-box; margin: 0; padding: 0; }
  html, body {
    width: 1200px;
    height: 1000px;
    overflow: hidden;
    background: var(--page-bg);
  }
  .canvas {
    position: relative;
    width: 1200px;
    height: 1000px;
  }
  .book-cover {
    position: absolute;
    left: 320px;
    top: 100px;
    width: 560px;
    height: 800px;
    background: var(--cover-bg);
    overflow: hidden;
    box-shadow: 0 6px 24px rgba(0, 0, 0, 0.12);
    font-family: "Montserrat", sans-serif;
  }
  .title {
    position: absolute;
    left: 60px;
    top: 150px;
    display: flex;
    align-items: center;
  }
  .title-words {
    display: flex;
    flex-direction: column;
    color: var(--ink-grey);
    font-weight: 400;
    font-size: 44px;
    line-height: 0.92;
    letter-spacing: -0.5px;
    text-transform: uppercase;
  }
  .title-seo {
    margin-left: 10px;
    color: var(--brand-blue);
    font-weight: 800;
    font-size: 98px;
    line-height: 1;
    letter-spacing: -2px;
  }
  .subtitle {
    position: absolute;
    left: 0;
    right: 0;
    top: 258px;
    padding-left: 30px;
    text-align: center;
    color: var(--ink-grey);
    font-style: italic;
    font-weight: 500;
    font-size: 13px;
    letter-spacing: 1.2px;
  }
  .cover-art {
    position: absolute;
    left: 0;
    top: 360px;
    width: 560px;
    height: 400px;
  }
  .author {
    position: absolute;
    left: 0;
    right: 0;
    bottom: 24px;
    text-align: center;
    color: var(--brand-blue);
    font-weight: 300;
    font-size: 42px;
    letter-spacing: 5px;
    text-transform: uppercase;
  }
</style>
</head>
<body>
<main class="canvas">
  <article class="book-cover">
    <h1 class="title">
      <span class="title-words">
        <span>Otter</span>
        <span>Ambush</span>
      </span>
      <span class="title-seo">SEO</span>
    </h1>
    <p class="subtitle">For Managed Service Providers</p>

    <svg class="cover-art" viewBox="0 0 560 400" aria-hidden="false">
      <defs>
        <linearGradient id="photoTone" x1="0" y1="0" x2="0.3" y2="1">
          <stop offset="0" stop-color="var(--photo-light)"/>
          <stop offset="0.5" stop-color="var(--photo-mid)"/>
          <stop offset="1" stop-color="var(--photo-dark)"/>
        </linearGradient>
      </defs>

      <!-- upper band and right diagonal band -->
      <polygon class="band band-top" points="150,28 330,28 362,52 150,52" fill="var(--brand-blue)"/>
      <polygon class="band band-right" points="330,28 372,28 556,208 528,236" fill="var(--brand-blue)"/>
      <polygon class="band band-right-inner" points="316,44 332,44 520,228 510,238" fill="var(--brand-blue-deep)"/>

      <!-- photo area -->
      <g role="img" aria-label="Photograph of a wild animal wading through a river, tinted with a red and blue glitch effect">
        <polygon class="photo-area" points="62,52 350,52 530,228 420,372 62,372" fill="url(#photoTone)"/>
      </g>

      <!-- left chevron -->
      <polygon class="chevron chevron-outer" points="0,84 44,84 190,230 58,372 0,372 130,230" fill="var(--brand-blue)"/>
      <polygon class="chevron chevron-stripe" points="30,84 44,84 190,230 58,372 44,372 176,230" fill="var(--white)"/>
      <polygon class="chevron chevron-inner" points="50,84 80,84 226,230 94,372 64,372 196,230" fill="var(--brand-blue-deep)"/>
    </svg>

    <p class="author">Dean Harrow</p>
  </article>
</main>
</body>
</html>
```